TAILWIND FIELDS Pet Resorts Outdoor Signage

4 x 8 outdoor signage design for our two locations

Target Market(s)

Existing and New Customers

Industry/Entity Type

Pet Care

Font styles to use
Sans Serif

Colors

Designer to choose colors to be used in the design.

```html
<!DOCTYPE html>
<html lang="en">
<head>
<meta charset="utf-8">
<title>Tailwind Fields Pet Resort – Outdoor Sign</title>
<link rel="stylesheet" href="https://fonts.googleapis.com/css2?family=League+Spartan:wght@700;800&family=Jost:wght@500;600&display=swap">
<style>
  :root {
    --ink: #454545;
    --teal: #4a8fa6;
    --white: #ffffff;
    --bar: #4a4a4b;
    --photo-light: #f1e2c6;
    --photo-mid: #d7a566;
  }
  * { margin: 0; padding: 0; box-sizing: border-box; }
  html, body {
    width: 1200px;
    height: 666px;
    overflow: hidden;
    background: var(--white);
  }
  .sign {
    position: relative;
    width: 1200px;
    height: 666px;
    overflow: hidden;
    background: var(--white);
    color: var(--ink);
    font-family: "Jost", "Futura", sans-serif;
  }
  .brand {
    position: absolute;
    left: 44px;
    top: 70px;
    width: 380px;
  }
  .brand-dot {
    display: block;
    width: 120px;
    height: 120px;
    border-radius: 50%;
    background: var(--teal);
    margin-bottom: 28px;
  }
  .brand-name {
    font-family: "League Spartan", sans-serif;
    font-weight: 800;
    font-size: 74px;
    line-height: 0.98;
    color: var(--ink);
    letter-spacing: 1px;
  }
  .headline {
    position: absolute;
    left: 498px;
    top: 84px;
    font-family: "League Spartan", sans-serif;
    font-weight: 800;
    font-size: 112px;
    line-height: 1;
    letter-spacing: 3px;
    color: var(--ink);
    white-space: nowrap;
  }
  .tagline-band {
    position: absolute;
    left: 428px;
    top: 201px;
    width: 772px;
    height: 67px;
    background: var(--teal);
  }
  .tagline {
    position: absolute;
    left: 527px;
    top: 201px;
    height: 67px;
    line-height: 70px;
    font-family: "League Spartan", sans-serif;
    font-weight: 700;
    font-size: 50px;
    letter-spacing: 6px;
    color: var(--white);
    white-space: nowrap;
  }
  .services {
    position: absolute;
    left: 452px;
    top: 284px;
    list-style: none;
    font-weight: 600;
    font-size: 35px;
    line-height: 47px;
    color: var(--ink);
    white-space: nowrap;
  }
  .services li::before {
    content: "•";
    margin-right: 3px;
  }
  .pet-photo {
    position: absolute;
    left: 770px;
    top: 271px;
    width: 396px;
    height: 277px;
    border-radius: 40% 40% 10% 10% / 50% 50% 8% 8%;
    background: radial-gradient(ellipse at 45% 45%, var(--photo-mid) 0%, var(--photo-light) 60%, var(--white) 100%);
  }
  .contact-bar {
    position: absolute;
    left: 0;
    top: 550px;
    width: 1200px;
    height: 116px;
    background: var(--bar);
    color: var(--white);
    font-weight: 600;
    font-size: 50px;
    line-height: 116px;
    text-align: center;
    letter-spacing: 0.5px;
    white-space: nowrap;
  }
  .contact-bar .divider { margin: 0 14px; }
</style>
</head>
<body>
  <main class="sign">
    <div class="brand">
      <span class="brand-dot"></span>
      <div class="brand-name">TAILWIND<br>FIELDS</div>
    </div>

    <h1 class="headline">PET RESORT</h1>
    <div class="tagline-band"></div>
    <p class="tagline">ALL BREED FRIENDLY</p>

    <ul class="services">
      <li>Boarding</li>
      <li>Daycare</li>
      <li>Training</li>
      <li>Full-Service Salon</li>
      <li>Pet Taxi &amp; More</li>
    </ul>

    <div class="pet-photo" role="img" aria-label="Photo of a golden retriever lying down with three small chihuahuas beside it"></div>

    <footer class="contact-bar">
      <span class="phone">905-555-0142</span><span class="divider">|</span><span class="web">WWW.TAILWINDFIELDS.CA</span>
    </footer>
  </main>
</body>
</html>
```